3 Business Card designs for a company with multiple services

We are a company that has 3 main services:

1) Security - CCTV & Alarm Sepcialists
2) Broadcast - Broadcast Sales and Technical Services
3) Distribution - Quality Products, Quality Service

The broadcast service is for Video Broadcast.

I will include our logos for each service.

I would like to also create a business card design for 5QM in general (see main logo).

Each card will be two-sided. On the front I would think it would include Logo, Name, Posistion and Mobile (and possibly email). And possibly our main number (which may be something like 1800 639 415)

On the back it MUST include a "lined" section to be able to write short quotes / prices.

Then include more details like Phone: 1800 639 415 Fax: 1800 639 417 Postal: PO Box 317, Tallowbrook, QLD Australia 4219 Website: www.5qm.com.au

We would like a fresh, inovative card design with that "wow check this out" feel about it.

Look forward to seeing what you can do! :)

Corin

Industry/Entity Type

Business

Requirements
Must have
• Quote section on the back!
Editable files.

```html
<!DOCTYPE html>
<html lang="en">
<head>
<meta charset="utf-8">
<title>5QM Business Card</title>
<link href="https://fonts.googleapis.com/css2?family=PT+Sans:wght@400;700&display=swap" rel="stylesheet">
<style>
  :root {
    --stage: #1c1c1c;
    --card: #d1d2d4;
    --mark: #2a2a2c;
    --ink: #1e1e1e;
    --ink-soft: #4a4a4c;
    --rule: #8c8d90;
  }
  html, body {
    margin: 0;
    padding: 0;
    width: 1200px;
    height: 934px;
    overflow: hidden;
    background: var(--stage);
    font-family: "PT Sans", "Helvetica Neue", Arial, sans-serif;
  }
  .canvas {
    position: relative;
    width: 1200px;
    height: 934px;
  }
  .card {
    position: absolute;
    background: var(--card);
    border-radius: 16px;
    box-shadow: 0 6px 14px rgba(0,0,0,0.6);
  }
  .card--front { left: 250px; top: 42px; width: 695px; height: 391px; }
  .card--back  { left: 250px; top: 496px; width: 698px; height: 394px; }

  .brand {
    position: absolute;
    display: flex;
    align-items: center;
  }
  .brand__square {
    background: var(--mark);
    flex: none;
  }
  .brand__name {
    color: var(--ink);
    font-weight: 700;
    line-height: 1;
  }
  .card--front .brand { left: 44px; top: 52px; gap: 24px; }
  .card--front .brand__square { width: 80px; height: 80px; }
  .card--front .brand__name { font-size: 76px; }
  .card--back .brand { left: 44px; top: 45px; gap: 12px; }
  .card--back .brand__square { width: 38px; height: 38px; }
  .card--back .brand__name { font-size: 36px; }

  .person {
    position: absolute;
    left: 58px;
    top: 240px;
    color: var(--ink);
  }
  .person__name { font-size: 21px; font-weight: 700; line-height: 1.1; }
  .person__role { font-size: 17px; color: var(--ink-soft); line-height: 1.2; }
  .person__contact { margin-top: 26px; font-size: 16px; color: var(--ink-soft); line-height: 1.3; }

  .details {
    position: absolute;
    left: 60px;
    top: 227px;
    font-size: 16px;
    line-height: 1.35;
    color: var(--ink-soft);
  }
  .details__postal { margin-bottom: 20px; }

  .quote-lines {
    position: absolute;
    left: 373px;
    top: 86px;
    width: 284px;
    height: 266px;
  }
</style>
</head>
<body>
<main class="canvas">
  <section class="card card--front" aria-label="Card front">
    <div class="brand">
      <span class="brand__square"></span>
      <span class="brand__name">5QM</span>
    </div>
    <div class="person">
      <div class="person__name">Corin Marsh</div>
      <div class="person__role">Director</div>
      <div class="person__contact">
        <div>M. 1800 639 417</div>
        <div>corin@5qm.com.au</div>
      </div>
    </div>
  </section>

  <section class="card card--back" aria-label="Card back">
    <div class="brand">
      <span class="brand__square"></span>
      <span class="brand__name">5QM</span>
    </div>
    <svg class="quote-lines" viewBox="0 0 284 266" aria-label="Lined quote section">
      <g stroke="var(--rule)" stroke-width="1.2">
        <line x1="0" y1="1" x2="284" y2="1"/>
        <line x1="0" y1="38" x2="284" y2="38"/>
        <line x1="0" y1="76" x2="284" y2="76"/>
        <line x1="0" y1="113" x2="284" y2="113"/>
        <line x1="0" y1="152" x2="284" y2="152"/>
        <line x1="0" y1="189" x2="284" y2="189"/>
        <line x1="0" y1="227" x2="284" y2="227"/>
        <line x1="0" y1="265" x2="284" y2="265"/>
      </g>
    </svg>
    <div class="details">
      <div class="details__postal">PO Box 317, Tallowbrook,<br>QLD Australia 4219</div>
      <div>P. 1800 639 415</div>
      <div>F. 1800 639 417</div>
      <div>www.5qm.com.au</div>
    </div>
  </section>
</main>
</body>
</html>
```